Label Design For Vitamin C Serum for Larkwind Skin Care

I need a label design for a bottle similar to this:

https://www.tradelumo-market.example/item/Sample-Face-Serum-Bottle/50000000001.html

Industry/Entity Type

Skin Care Product

Font styles to use
Other font styles liked:
• use logo and use anything standard for label text

Colors
000000

Requirements
Must have
• 20% Vitamin C Brightening Serum
• 30 ML
• On back of label:
• Vitamin C serum is a potent antioxidant designed to help minimize the damaging effects of free oxygen radicals.
• This formulation will help restore skin tone and youthful appearance to the skin.
• Apply 2-3 drops of serum to desired areas. Massage with fingertips.
Nice to have
• I want to use the GOLD LOGO with BLACK LABEL

```html
<!DOCTYPE html>
<html lang="en">
<head>
<meta charset="utf-8">
<title>Larkwind Skin Care – 20% Vitamin C Brightening Serum Label</title>
<link rel="stylesheet" href="https://fonts.googleapis.com/css2?family=Oswald:wght@500&family=Share+Tech+Mono&display=swap">
<style>
  :root {
    --page: #ffffff;
    --label: #0b0b0b;
    --gold: #c9a24a;
    --amber: #e3a32a;
    --white: #f4f4f4;
  }
  * { margin: 0; padding: 0; box-sizing: border-box; }
  html, body {
    width: 1200px;
    height: 2618px;
    overflow: hidden;
    background: var(--page);
  }
  .canvas {
    position: relative;
    width: 1200px;
    height: 2618px;
  }
  .label {
    position: absolute;
    left: 100px;
    top: 669px;
    width: 1000px;
    height: 1280px;
    background: var(--label);
    overflow: hidden;
  }
  .brand {
    position: absolute;
    left: 60px;
    top: 60px;
    height: 1160px;
    writing-mode: vertical-rl;
    transform: rotate(180deg);
    text-align: left;
    white-space: nowrap;
    font-family: "Oswald", "Arial Narrow", sans-serif;
    font-weight: 500;
    font-size: 104px;
    letter-spacing: 0.04em;
    line-height: 1;
    color: var(--gold);
  }
  .product {
    position: absolute;
    right: 36px;
    top: 717px;
    text-align: right;
    color: var(--white);
    line-height: 1;
    white-space: nowrap;
  }
  .product-strength,
  .product-active {
    font-family: "Oswald", "Arial Narrow", sans-serif;
    font-weight: 500;
  }
  .product-strength { font-size: 84px; }
  .product-active { font-size: 92px; margin-top: 6px; }
  .product-benefit {
    font-family: "Share Tech Mono", monospace;
    font-size: 56px;
    margin-top: 6px;
  }
  .product-type {
    font-family: "Share Tech Mono", monospace;
    font-size: 66px;
    color: var(--amber);
    letter-spacing: 0.3em;
    margin-right: -0.3em;
    margin-top: 4px;
  }
  .volume {
    position: absolute;
    right: 36px;
    top: 1110px;
    font-family: "Share Tech Mono", monospace;
    font-size: 92px;
    color: var(--white);
    line-height: 1;
  }
</style>
</head>
<body>
  <main class="canvas">
    <section class="label">
      <p class="brand">Larkwind Skin Care</p>
      <div class="product">
        <p class="product-strength">20%</p>
        <p class="product-active">VITAMIN C</p>
        <p class="product-benefit">BRIGHTENING</p>
        <p class="product-type">SERUM</p>
      </div>
      <p class="volume">30ml</p>
    </section>
  </main>
</body>
</html>
```